Pitch Deck and business cards for Virtual Reality Startup

We need a redesign of our pitch deck to be funky, creative and interactive with animated graphics inline with our product (VR training)
Note: the design does not have to be orange that's just a template of the information we're sending you so we would like to see other colours also.

Target Market(s)

Investors

Industry/Entity Type

Media

Contact Information for Business Card

logo, Name, title, address, telephone, email, website

Font styles to use
Other font styles liked:
• funky but readable

Colors

Designer to choose colors to be used in the design.

Requirements
Must have
• Exciting non traditional design that fits a new, innovative, exciting and interactive technology
Nice to have
• .
Should not have
• traditional look and feel.

```html
<!DOCTYPE html>
<html lang="en">
<head>
<meta charset="utf-8">
<title>NOVA XR — Pitch Deck</title>
<link href="https://fonts.googleapis.com/css2?family=Oswald:wght@500;700&family=Bangers&family=Roboto:wght@400;700&display=swap" rel="stylesheet">
<style>
:root{
  --stage:#3a3a3c;
  --blue:#0b5cb5;
  --blue-deep:#084a94;
  --ink:#1f2430;
  --white:#ffffff;
  --shade:#e3e7ee;
  --muted:#6b7280;
  --role:#cfd4dc;
}
*{box-sizing:border-box;margin:0;padding:0}
html,body{width:840px;height:1200px;overflow:hidden;background:var(--stage)}
.deck{position:relative;width:840px;height:1200px}
.slide{position:absolute;width:408px;height:232px;background:var(--blue);overflow:hidden}
.col-a{left:6px}.col-b{left:424px}
.row-1{top:4px}.row-2{top:244px}.row-3{top:484px}.row-4{top:724px}.row-5{top:964px}
.panel{position:absolute;inset:10px 10px 12px 10px;background:var(--white);border-radius:22px;overflow:hidden}
.corner-disc{position:absolute;width:78px;height:78px;border-radius:50%;background:var(--shade)}
.disc-tr{right:-14px;top:-12px}
.disc-bl{left:-14px;bottom:-16px}
.title{position:absolute;left:0;right:0;text-align:center;font-family:"Oswald",sans-serif;font-weight:700;font-size:21px;letter-spacing:.2px;color:var(--ink);line-height:1}
.title.blue{color:var(--blue)}
.brand{position:absolute;left:0;right:0;bottom:10px;display:flex;justify-content:center;align-items:center;gap:5px;font-family:"Oswald",sans-serif;font-weight:700;font-size:14px;color:var(--ink);letter-spacing:1px}
.brand::before{content:"";width:8px;height:8px;background:var(--ink)}
.placeholder{position:absolute}
/* slide 1 */
.hero-photo{left:0;top:0;width:100%;height:132px;background:linear-gradient(120deg,#2a2622,#6b4a30 55%,#1c1a1a)}
.hero-person{right:0;top:20px;width:200px;height:190px;background:linear-gradient(160deg,#9a7a64,#3d4656);border-radius:40% 40% 0 0}
.award-badge{position:absolute;left:22px;top:12px;width:44px;height:46px;background:#cfcfcf;border-radius:4px}
.hero-brand{position:absolute;left:20px;top:78px;font-family:"Oswald",sans-serif;font-weight:700;font-size:28px;color:var(--white);letter-spacing:2px;display:flex;align-items:center;gap:6px}
.hero-brand::after{content:"";width:10px;height:10px;background:var(--white)}
.hero-title{position:absolute;left:22px;top:142px;font-family:"Oswald",sans-serif;font-weight:700;font-size:20px;line-height:1.05;color:var(--ink)}
.hero-title .blue{color:var(--blue)}
/* slide 2 */
.clipping{position:absolute;left:118px;top:48px;width:148px;height:126px;background:var(--white);box-shadow:0 1px 4px rgba(0,0,0,.3);padding:5px}
.clip-head{font-family:"Roboto",sans-serif;font-weight:700;font-size:6px;line-height:1.2;color:var(--ink)}
.clip-by{font-family:"Roboto",sans-serif;font-size:3.5px;color:var(--muted);margin:2px 0}
.clip-photo{width:100%;height:86px;background:linear-gradient(135deg,#3f6b3a,#a9b2a0 60%,#2d3a2a)}
.clip-cap{font-family:"Roboto",sans-serif;font-size:3.5px;color:var(--muted);margin-top:2px}
/* slide 3 */
.problem-text{position:absolute;left:0;right:0;top:72px;text-align:center;font-family:"Bangers",sans-serif;font-size:23px;line-height:1.02;color:var(--ink);letter-spacing:.5px}
.problem-text .blue{color:var(--blue)}
.tag{position:absolute;left:160px;top:152px;background:var(--ink);color:var(--white);font-family:"Oswald",sans-serif;font-weight:700;font-size:12px;padding:3px 8px;transform:skewX(-8deg)}
/* slide 4 */
.class-photo{left:70px;top:50px;width:272px;height:118px;border:2px solid var(--blue);background:linear-gradient(120deg,#c7cdd4,#7a5a4a 60%,#d9d3c8)}
/* slide 5 */
.video{left:84px;top:40px;width:238px;height:134px;border:2px solid var(--blue-deep);background:radial-gradient(ellipse at 40% 30%,#b04a9c,#5a1c4a 55%,#16060f)}
/* slide 6 */
.vr-people{right:0;bottom:0;width:200px;height:140px;background:linear-gradient(150deg,#d8d8d8,#8a6a58 60%,#2a2a2a);border-radius:60px 0 0 0}
.bullets{position:absolute;list-style:none;font-family:"Oswald",sans-serif;font-weight:700;font-size:11px;line-height:1.05}
.bullets li{display:flex;gap:6px;align-items:flex-start;margin-bottom:9px}
.bullets li::before{content:"";flex:none;width:16px;height:7px;margin-top:2px;background:var(--blue);border-radius:2px 2px 4px 4px}
.bullets.blue{color:var(--blue)}
.bullets.ink{color:var(--ink)}
.bullets.ink li{margin-bottom:7px;align-items:center}
.bullets.ink li::before{margin-top:0}
/* slide 7 */
.member{position:absolute;width:100px;height:36px}
.member-card{position:absolute;left:12px;top:0;right:0;bottom:0;background:var(--ink);clip-path:polygon(0 0,100% 0,92% 100%,0 100%);color:var(--white);padding:4px 9px 0 18px;display:flex;flex-direction:column;justify-content:center}
.member-avatar{position:absolute;left:0;top:6px;width:24px;height:24px;border-radius:50%;background:#b89a86;border:2px solid var(--white);z-index:1}
.member b{display:block;font-family:"Oswald",sans-serif;font-weight:700;font-size:7px;line-height:1.05}
.member span{display:block;font-family:"Roboto",sans-serif;font-size:4px;line-height:1.15;margin-top:1px;color:var(--role)}
/* slide 8 */
.step{position:absolute;width:68px;height:32px;background:var(--blue);clip-path:polygon(0 0,100% 0,88% 100%,12% 100%);color:var(--white);font-family:"Oswald",sans-serif;font-weight:700;font-size:5.5px;display:flex;align-items:center;justify-content:center;text-align:center;line-height:1.15;padding:0 10px}
/* slide 10 */
.qmark{position:absolute;left:144px;top:44px;width:100px;height:120px}
.qmark .disc{position:absolute;width:52px;height:52px;border-radius:50%;background:var(--shade)}
.qmark .glyph{position:absolute;left:0;right:0;top:0;text-align:center;font-family:"Oswald",sans-serif;font-weight:700;font-size:104px;line-height:112px;color:var(--white);-webkit-text-stroke:5px var(--ink)}
</style>
</head>
<body>
<main class="deck">

  <section class="slide col-a row-1">
    <div class="panel">
      <div class="placeholder hero-photo" role="img" aria-label="Dimly lit bar with shelves of bottles"></div>
      <div class="placeholder hero-person" role="img" aria-label="Young man wearing a VR headset"></div>
      <div class="award-badge" aria-hidden="true"></div>
      <div class="hero-brand">NOVA XR</div>
      <h1 class="hero-title">THE FUTURE OF<br><span class="blue">HOSPITALITY</span><br>TRAINING</h1>
    </div>
  </section>

  <section class="slide col-b row-1">
    <div class="panel">
      <div class="corner-disc disc-tr"></div><div class="corner-disc disc-bl"></div>
      <h2 class="title" style="top:22px">ANNA'S STORY...</h2>
      <article class="clipping">
        <p class="clip-head">Apprentice's charges upgraded after 'one-punch' victim dies in Port Allan</p>
        <p class="clip-by">By staff reporters, updated this morning</p>
        <div class="clip-photo" role="img" aria-label="News photo of a young man outside a courthouse"></div>
        <p class="clip-cap">Photo: the accused leaves court after the hearing.</p>
      </article>
      <div class="brand">NOVA XR</div>
    </div>
  </section>

  <section class="slide col-a row-2">
    <div class="panel">
      <div class="corner-disc disc-tr"></div><div class="corner-disc disc-bl"></div>
      <h2 class="title blue" style="top:20px">THE PROBLEM</h2>
      <p class="problem-text">TRADITIONAL TRAINING<br>DOES <span class="blue">NOT PREPARE</span> STAFF<br>TO BE</p>
      <span class="tag">JOB READY</span>
      <div class="brand">NOVA XR</div>
    </div>
  </section>

  <section class="slide col-b row-2">
    <div class="panel">
      <div class="corner-disc disc-tr"></div><div class="corner-disc disc-bl"></div>
      <h2 class="title" style="top:20px">TRADITIONAL TRAINING</h2>
      <div class="placeholder class-photo" role="img" aria-label="Bored student resting head on a classroom desk"></div>
      <div class="brand">NOVA XR</div>
    </div>
  </section>

  <section class="slide col-a row-3">
    <div class="panel">
      <div class="corner-disc disc-tr"></div><div class="corner-disc disc-bl"></div>
      <h2 class="title blue" style="top:12px">PLAY VIDEO</h2>
      <div class="placeholder video" role="img" aria-label="Embedded product video"></div>
      <div class="brand">NOVA XR</div>
    </div>
  </section>

  <section class="slide col-b row-3">
    <div class="panel">
      <div class="corner-disc disc-tr"></div><div class="corner-disc disc-bl"></div>
      <h2 class="title" style="top:16px;left:150px;right:auto;width:200px">VIRTUAL REALITY<br>TRAINING</h2>
      <div class="placeholder vr-people" role="img" aria-label="Two people smiling while using VR headsets"></div>
      <ul class="bullets blue" style="left:50px;top:70px">
        <li>RETENTION OF<br>KNOWLEDGE</li>
        <li>REAL-LIFE<br>EXPERIENCES</li>
        <li>IMMERSIVE &amp;<br>ENGAGING</li>
      </ul>
      <div class="brand" style="right:190px">NOVA XR</div>
    </div>
  </section>

  <section class="slide col-a row-4">
    <div class="panel">
      <div class="corner-disc disc-tr"></div><div class="corner-disc disc-bl"></div>
      <h2 class="title blue" style="top:14px">WHAT MAKES US UNIQUE?</h2>
      <div class="member" style="left:56px;top:64px"><div class="member-avatar" role="img" aria-label="Portrait of Owen Hartley"></div><div class="member-card"><b>OWEN HARTLEY</b><span>Co Founder and CEO</span></div></div>
      <div class="member" style="left:158px;top:64px"><div class="member-avatar" role="img" aria-label="Portrait of Dr Lena Markovic"></div><div class="member-card"><b>DR LENA<br>MARKOVIC</b><span>Learning and Development Strategist</span></div></div>
      <div class="member" style="left:260px;top:64px"><div class="member-avatar" role="img" aria-label="Portrait of Ruth Calder"></div><div class="member-card"><b>RUTH CALDER</b><span>Co Founder, Education and Content Director</span></div></div>
      <div class="member" style="left:56px;top:106px"><div class="member-avatar" role="img" aria-label="Portrait of Marco Bellini"></div><div class="member-card"><b>MARCO BELLINI</b><span>360 Film and Post-Production Expert</span></div></div>
      <div class="member" style="left:158px;top:106px"><div class="member-avatar" role="img" aria-label="Portrait of Sofia Verano"></div><div class="member-card"><b>SOFIA<br>VERANO</b><span>Learning Designer</span></div></div>
      <div class="member" style="left:260px;top:106px"><div class="member-avatar" role="img" aria-label="Portrait of Kenji Arata"></div><div class="member-card"><b>KENJI<br>ARATA</b><span>Programmer and Game Developer</span></div></div>
      <div class="brand">NOVA XR</div>
    </div>
  </section>

  <section class="slide col-b row-4">
    <div class="panel">
      <div class="corner-disc disc-tr"></div><div class="corner-disc disc-bl"></div>
      <h2 class="title" style="top:14px">WHAT MAKES US UNIQUE?</h2>
      <div class="step" style="left:84px;top:50px">RESEARCH TOPICS</div>
      <div class="step" style="left:164px;top:50px">CREATE CONTENT</div>
      <div class="step" style="left:244px;top:50px">LEARNING DESIGN</div>
      <div class="step" style="left:84px;top:88px">360 FILM PRODUCTION</div>
      <div class="step" style="left:164px;top:88px">360 POST PRODUCTION</div>
      <div class="step" style="left:244px;top:88px">INTERACTIVE GAMING DEVELOPMENT</div>
      <div class="step" style="left:124px;top:126px">TESTING</div>
      <div class="step" style="left:204px;top:126px">RELEASE</div>
      <div class="brand">NOVA XR</div>
    </div>
  </section>

  <section class="slide col-a row-5">
    <div class="panel">
      <div class="corner-disc disc-tr"></div><div class="corner-disc disc-bl"></div>
      <h2 class="title blue" style="top:16px">OUR ASK</h2>
      <ul class="bullets ink" style="left:108px;top:74px">
        <li>INTRODUCTIONS</li>
        <li>FUNDING</li>
        <li>INVESTORS</li>
      </ul>
      <div class="brand">NOVA XR</div>
    </div>
  </section>

  <section class="slide col-b row-5">
    <div class="panel">
      <div class="corner-disc disc-tr"></div><div class="corner-disc disc-bl"></div>
      <h2 class="title blue" style="top:16px">QUESTIONS</h2>
      <div class="qmark">
        <div class="disc" style="left:4px;top:10px"></div>
        <div class="disc" style="left:50px;top:60px"></div>
        <div class="glyph">?</div>
      </div>
      <div class="brand">NOVA XR</div>
    </div>
  </section>

</main>
</body>
</html>
```